Business Card Design and Stationary design for consulting firm

Harbourline Sourcing are looking for a new business card design and a design for their A4 letterhead / A4 invoices.

We are seeking to heavily increase our brand awareness and require a business card that's professional in appearance but also shows flare and innovation. A card design that people will remember.

About Us
Harbourline Sourcing are `The Sourcing Crew’.
Our mission is to be one of Australia’s greatest companies. Our aim is to help our customers achieve the best result from their purchasing experience.

Our Requirement:
• IMPACT! IMPACT! IMPACT!
• BUSINESS & PROFESSIONAL LOOKING

• Our business colours are orange, blue and green (See the logo attached).

We have provided an Art Design specification (attached) that needs to be followed for you to win the design. This also has the font, which is used on the logo.

We are after a two sided business card

Side One should have the:
The company Logo
The Sourcing Crew
www.harbourlinesourcing.com.au
Procure | Personnel | Probity & Privacy
Sydney | Melbourne | Adelaide | Brisbane

Side Two
Logo (optional)
Harbourline Sourcing (optional)
Employee details (details listed below)

The above format is our preferred option, but if you think you can come up with something better, feel free to put it forward.

We are leaving the design up to you, but it must incorporate the logo.

We will need a template that we can change the employee details on, as we will be adding more staff over the coming months.

The details below are for one employee per card with the same design.
------------------------

Employee Details:

Marcus Del Arroyo MBA, MMgmtStratProc
Principal Consultant
0491 372 618
Marcus@harbourlinesourcing.com.au

Brianna Tolley
Consulting Manager
0462 915 308
Brianna@harbourlinesourcing.com.au

Our website is www.harbourlinesourcing.com.au

The Letterhead / invoice needs to incorporate:
the company Logo
The Sourcing Crew
Sydney | Melbourne | Adelaide | Brisbane but otherwise the design is over to you.

This file needs to be delivered in word format as other detail will be added to the documents.

We look forward to you award winning designs. If you require any further information please feel free to contact us.

Regards
Harbourline Sourcing

Target Market(s)

Our Target market is companies with 80+ employees. The market we segment is heavily male based, between the ages of 35-55 years of age.

Industry/Entity Type

Consulting

Contact Information for Business Card

See Project Description

Font styles to use
Other font styles liked:
• See Art Specification

Requirements
Must have
• Company Colours, See Project Description
Should not have
• Be outside the Art specification guidelines

```html
<!DOCTYPE html>
<html lang="en">
<head>
<meta charset="utf-8">
<title>Harbourline Sourcing – Letterhead and Invoice</title>
<link href="https://fonts.googleapis.com/css2?family=Open+Sans:wght@400;600;700&display=swap" rel="stylesheet">
<style>
:root{
  --backdrop:#a9abad;
  --paper:#ffffff;
  --ink:#333333;
  --ink-soft:#555555;
  --blue:#2a7fc9;
  --green:#4aa53a;
  --orange:#f08a24;
  --bar:#3a3a3a;
  --row-dark:#e1e2e3;
  --row-light:#efefef;
}
*{box-sizing:border-box;margin:0;padding:0}
html,body{width:1200px;height:888px;overflow:hidden}
body{background:var(--backdrop);font-family:"Open Sans",Arial,sans-serif;color:var(--ink);position:relative}
.sheet{position:absolute;top:114px;width:455px;height:644px;background:var(--paper);overflow:hidden;box-shadow:0 2px 6px rgba(0,0,0,.25)}
.sheet--letter{left:142px}
.sheet--invoice{left:643px}
.abs{position:absolute}
.brand{display:flex;align-items:center;gap:5px;font-weight:600;font-size:9px;color:var(--ink-soft);letter-spacing:.3px;white-space:nowrap}
.brand__dot{width:9px;height:9px;border-radius:50%;background:var(--blue)}
.contact{font-size:5.6px;line-height:11px;color:var(--ink)}
.contact svg{width:6px;height:6px;vertical-align:-1px;margin-right:5px;fill:var(--ink)}
.recipient{font-size:7.8px;line-height:10.6px}
.recipient strong{font-weight:700}
.body-copy{width:334px;font-size:7.3px;line-height:10.8px;text-align:justify}
.body-copy p{margin-bottom:10.8px}
.signoff{font-size:7.8px;line-height:10.6px}
.footer-bar{height:8px;width:334px;background:var(--bar);color:#fff;font-size:5.8px;font-weight:600;line-height:8px;display:flex;justify-content:space-between;padding:0 17px 0 12px;white-space:nowrap}
.people-band{left:0;top:598px;width:455px;height:46px;background:linear-gradient(90deg,var(--blue),var(--orange),var(--green),var(--blue),var(--orange),var(--green),var(--blue))}
.invoice-title{font-size:19px;letter-spacing:3.5px;color:var(--ink-soft);font-weight:600}
.company-meta{right:51px;text-align:right;font-size:5.4px;line-height:8px}
.company-meta strong{font-weight:700}
.company-meta svg{width:5px;height:5px;margin-left:4px;vertical-align:-0.5px;fill:var(--ink)}
.bill-to{font-size:8.6px;line-height:10.8px}
.bill-to strong{font-weight:700}
.table-head{left:0;top:236px;width:455px;height:20px;background:var(--blue);color:#fff;font-size:7.5px;font-weight:700;line-height:20px;padding:0 49px 0 64px;display:flex;justify-content:space-between}
.row{left:0;width:455px;padding:0 52px 0 64px;display:flex;justify-content:space-between;align-items:center;font-size:7.6px}
.row--dark{background:var(--row-dark)}
.row--light{background:var(--row-light)}
.row b{font-weight:700}
.row .amt{font-size:7px;font-weight:700}
.totals{left:250px;width:205px;display:flex;align-items:center;justify-content:space-between;padding:0 52px 0 24px;font-weight:700}
.totals--gst{top:369px;height:27px;background:var(--row-dark);font-size:8px}
.totals--grand{top:395px;height:21px;background:var(--blue);color:#fff;font-size:9px;padding-left:24px}
.totals--grand .grand{font-size:12px}
.payment{font-size:6.6px;line-height:8px}
.payment b{font-weight:700}
.bank{font-size:6.2px;line-height:9.2px}
.bank td{padding:0}
.bank td:first-child{width:62px}
.bank td:nth-child(2){width:8px}
.bank td:last-child{font-weight:700}
.questions{font-size:6.4px;font-weight:700}
.thanks{font-size:10px;font-weight:700;color:var(--blue);letter-spacing:.2px}
</style>
</head>
<body>

<section class="sheet sheet--letter" aria-label="Letterhead">
  <div class="abs brand" style="left:62px;top:73px"><span class="brand__dot"></span>Harbourline Sourcing</div>

  <div class="abs contact" style="left:290px;top:68px">
    <div><svg viewBox="0 0 10 10"><path d="M2 0l2 2-1 2c1 1 2 2 3 3l2-1 2 2-2 2C4 10 0 6 0 2z"/></svg>1300 582 104</div>
    <div><svg viewBox="0 0 10 10"><path d="M0 2h10v6H0z"/></svg>info@harbourlinesourcing.com.au</div>
    <div><svg viewBox="0 0 10 10"><path d="M1 9l8-8M3 3l2-2h1M7 7l-2 2H4" stroke="#333" stroke-width="1.5" fill="none"/></svg>www.<b>harbourlinesourcing</b>.com.au</div>
  </div>

  <div class="abs recipient" style="left:66px;top:180px">
    <strong>Mr. Daniel Hart</strong><br>Managing Director<br>USA Investor<br>100 E Main Street<br>USA
  </div>

  <div class="abs body-copy" style="left:66px;top:254px">
    <p>Lorem Ipsum is simply dummy text for printing and typesetting industry. Lorem Ipsum has been the industry’s standard dummy text since classical literature, discovered the undoubtable sorce. es from section 1.133 of “de Finibus Bonorum et Moloruthe 1500s, when an unknown printe t has suvived not only manual but also tandard dummy text since clhe leap ularised in the 1960s with the release of Letterline sheets coith the release of Letterline shntaining Lorem Ipsum pass and more recently with desktop publishing software like Folio Layout including version 6.9 of Lorem Ipsum.</p>
    <p>Country to popular belief, Lorem Ipsum is not simply random text. It has roots in a piece of sical Latin literature from 45 BC, making it over 2000 Virginia, looked up one of the most of the world classical literature, discovered the undoubtable sorce. es from section 1.133 of “de Finibus Bonorum et Moloruclassical literature, discovered the undoubtable sorce. es from section 1.133 of “de Finibus Bonorum et Molorum” ( The Extandard dummy text since clreme of Good and Even Cicero), written in 45 BC. This book is a treatise on the theory of ethics very popular during Renassiance.</p>
    <p>Thank you for being one of our valued customers.</p>
  </div>

  <div class="abs signoff" style="left:66px;top:490px"><strong>Name Here</strong><br>CEO</div>

  <div class="abs footer-bar" style="left:66px;top:571px">
    <span>Procure | Personnel | Probity &amp; Privacy</span>
    <span>Sydney | Melbourne | Adelaide | Brisbane</span>
  </div>

  <div class="abs people-band" role="img" aria-label="Row of figures in brand blue, orange and green"></div>
</section>

<section class="sheet sheet--invoice" aria-label="Invoice">
  <h1 class="abs invoice-title" style="left:54px;top:84px">INVOICE</h1>

  <div class="abs brand" style="right:48px;top:73px"><span class="brand__dot"></span>Harbourline Sourcing</div>

  <div class="abs company-meta" style="top:122px">
    <div><strong>ABN:</strong> 48392017563</div>
    <div><strong>ACN:</strong> 392 017 563</div>
    <div style="margin-top:6px">14 Carrow Street<br>Ridgeview, NSW Australia 2190</div>
    <div style="margin-top:2px">1300 582 104<svg viewBox="0 0 10 10"><path d="M2 0l2 2-1 2c1 1 2 2 3 3l2-1 2 2-2 2C4 10 0 6 0 2z"/></svg></div>
    <div>info@harbourlinesourcing.com.au<svg viewBox="0 0 10 10"><path d="M0 2h10v6H0z"/></svg></div>
    <div>www.<b>harbourlinesourcing</b>.com.au<svg viewBox="0 0 10 10"><path d="M1 9l8-8" stroke="#333" stroke-width="1.5"/></svg></div>
  </div>

  <div class="abs bill-to" style="left:64px;top:141px">
    INVOICE TO:<br><strong>Mr. Daniel Hart</strong><br>Demonstration Client<br>Unit 22, 1111 Somewhere Street<br>Northern Lights&nbsp; VIC&nbsp; 3456
  </div>

  <div class="abs table-head"><span>DESCRIPTION</span><span>AMOUNT</span></div>
  <div class="abs row row--dark" style="top:256px;height:28px;align-items:flex-start;padding-top:6px"><b>Description of&nbsp; Service</b><span class="amt" style="margin-top:3px">$ 500.00</span></div>
  <div class="abs row row--light" style="top:284px;height:28px"><span></span><span class="amt">$ 500.00</span></div>
  <div class="abs row row--dark" style="top:312px;height:29px"></div>
  <div class="abs row row--light" style="top:341px;height:28px;padding-right:49px">
    <b>Sub Total ex GST</b><span style="font-size:7px;margin-left:40px">10 days @ $ 100 ex GST</span><b style="margin-left:auto;font-size:8.2px">$ 1000.00</b>
  </div>

  <div class="abs totals totals--gst"><span>GST</span><span>$ 100.00</span></div>
  <div class="abs totals totals--grand"><span>TOTAL :</span><span class="grand">$ 9,900.00</span></div>

  <div class="abs payment" style="left:65px;top:406px">Make all payments by direct deposit to<br><b>Harbourline Sourcing Pty Limited</b></div>

  <div class="abs" style="left:65px;top:428px">
    <div class="bank" style="margin-bottom:2px">The company bank account details are:</div>
    <table class="bank">
      <tr><td>Banking Institution:</td><td></td><td>Southbank Mutual</td></tr>
      <tr><td>Account Name</td><td>:</td><td>Harbourline Sourcing Pty Limited</td></tr>
      <tr><td>BSB</td><td>:</td><td>064182</td></tr>
      <tr><td>Account Number</td><td>:</td><td>518273640</td></tr>
    </table>
  </div>

  <div class="abs questions" style="left:65px;top:500px">If you have any questions concerning this invoice, contact us</div>
  <div class="abs thanks" style="left:65px;top:521px">THANK YOU FOR YOUR BUSINESS!</div>

  <div class="abs footer-bar" style="left:64px;top:572px">
    <span>Procure | Personnel | Probity &amp; Privacy</span>
    <span>Sydney | Melbourne | Adelaide | Brisbane</span>
  </div>

  <div class="abs people-band" role="img" aria-label="Row of figures in brand blue, orange and green"></div>
</section>

</body>
</html>
```